Lantern Advisory Business Cards

We need a new layout for our business cards. We have a logo already. But we might be interested in only using the Lantern portion of the logo. It has been uploaded.

We would like cards that are not overly busy. Clean. Modern. Perhaps a gray color for one side.

On the back, we would like to have the lantern part of the logo and "Take the Leap, we've got you!"

Our business provides medics and safety training for corporate clients. Our website is www.lanternadvisoryllc.example.

Industry/Entity Type

Business

Contact Information for Business Card

We want include name, email address, cell phone, main line number, and website URL on the front. Use the following as an example: Marla Tobin, marla@lanternadvisoryllc.example, 402.318.7264 (cell), 402.947.315, and www.lanternadvisoryllc.example.

Font styles to use
Serif
Sans Serif

Requirements
Must have
• All required information. Back side logo with "Take the leap, we will catch you!"
Nice to have
• If possible, we would like to consider creating a card in a non-standard shape. Perhaps, the shape of a lantern. Just interested in understanding the option.

```html
<!DOCTYPE html>
<html lang="en">
<head>
<meta charset="utf-8">
<title>Lantern Advisory Business Cards</title>
<link rel="stylesheet" href="https://fonts.googleapis.com/css2?family=Raleway:wght@300;400;600;700&display=swap">
<style>
  :root {
    --backdrop: #d4d4d4;
    --card-light: #e8e8e6;
    --navy: #0f3a4e;
    --navy-raised: #17465c;
    --muted: #7d8a91;
    --white: #ffffff;
  }
  * { box-sizing: border-box; margin: 0; padding: 0; }
  html, body {
    width: 1200px; height: 900px; overflow: hidden;
    background: var(--backdrop);
    font-family: "Raleway", sans-serif;
  }
  .sheet {
    width: 1200px; height: 900px;
    display: flex; flex-direction: column;
    align-items: center; justify-content: center; gap: 60px;
  }
  .card {
    position: relative;
    width: 600px; height: 343px;
    border-radius: 3px;
    box-shadow: 0 2px 6px rgba(0,0,0,0.12);
    overflow: hidden;
  }
  .card--front { background: var(--card-light); color: var(--navy); }
  .card--back { background: var(--navy); color: var(--white); }

  .brand {
    position: absolute; top: 40px; right: 40px;
    display: flex; align-items: center; gap: 10px;
    font-weight: 600; font-size: 20px; letter-spacing: 0.02em;
  }
  .brand__dot {
    width: 14px; height: 14px; border-radius: 50%;
    background: currentColor;
  }
  .brand--front { color: var(--navy); }
  .brand--back { color: var(--navy-raised); font-size: 30px; top: 48px; right: 44px; }
  .brand--back .brand__dot { width: 20px; height: 20px; }

  .contact {
    position: absolute; left: 44px; top: 110px;
  }
  .contact__name { font-size: 24px; font-weight: 700; }
  .contact__role { font-size: 13px; font-weight: 300; color: var(--muted); margin-top: 2px; }
  .contact__web { font-size: 14px; font-weight: 700; margin-top: 4px; }
  .contact__row {
    display: flex; align-items: flex-start; gap: 10px;
    font-size: 12px; font-weight: 400; margin-top: 10px; line-height: 1.2;
  }
  .contact__icon {
    width: 16px; height: 16px; flex: none;
  }

  .tagline {
    position: absolute; left: 44px; bottom: 44px;
    font-size: 24px; font-weight: 400; color: var(--white);
  }
</style>
</head>
<body>
<main class="sheet">
  <section class="card card--front" aria-label="Card front">
    <div class="brand brand--front"><span class="brand__dot"></span>Lantern Advisory</div>
    <div class="contact">
      <div class="contact__name">Marla Tobin</div>
      <div class="contact__role">Designation</div>
      <div class="contact__web">www.lanternadvisoryllc.example</div>
      <div class="contact__row">
        <svg class="contact__icon" viewBox="0 0 16 16" aria-hidden="true">
          <circle cx="8" cy="8" r="8" fill="#0f3a4e"/>
          <path d="M5.3 4.2c.4-.3.9-.2 1.1.2l.7 1.3c.2.4.1.8-.2 1l-.5.4c.4.9 1.1 1.6 2 2l.4-.5c.3-.3.7-.4 1-.2l1.3.7c.4.2.5.7.2 1.1-.6.9-1.6 1.1-2.6.6-1.7-.8-3-2.1-3.8-3.8-.5-1-.3-2 .4-2.8z" fill="#e8e8e6"/>
        </svg>
        <span>402.318.7264<br>402.947.315</span>
      </div>
      <div class="contact__row">
        <svg class="contact__icon" viewBox="0 0 16 16" aria-hidden="true">
          <circle cx="8" cy="8" r="8" fill="#0f3a4e"/>
          <rect x="4" y="5" width="8" height="6" rx="1" fill="#e8e8e6"/>
          <path d="M4.3 5.4 8 8.3l3.7-2.9" stroke="#0f3a4e" stroke-width="0.9" fill="none"/>
        </svg>
        <span>marla@lanternadvisoryllc.example</span>
      </div>
    </div>
  </section>

  <section class="card card--back" aria-label="Card back">
    <div class="brand brand--back"><span class="brand__dot"></span>Lantern Advisory</div>
    <p class="tagline">Take the leap, we will catch you!</p>
  </section>
</main>
</body>
</html>
```